Quillmark painting

Am looking for a lawn sign design for my paintings company.
I also attached my business card a example

Phone number of the business +1(204)555-0187
Key words:Free estimates|pressure washing |Residential| Commercial | Interior | Exterior

```html
<!DOCTYPE html>
<html lang="en">
<head>
<meta charset="utf-8">
<title>Quillmark Painting — Lawn Sign</title>
<link rel="stylesheet" href="https://fonts.googleapis.com/css2?family=Poppins:wght@500;600;700;800&display=swap">
<style>
  :root {
    --page-bg: #a3a3a3;
    --ink-black: #000000;
    --brand-blue: #12b2e6;
    --sun-yellow: #f8e12b;
    --drip-light: #f2e65a;
    --drip-deep: #f0a820;
    --berry: #ae1a6b;
    --paper: #ffffff;
    --text-dark: #1a1a1a;
  }
  * { box-sizing: border-box; margin: 0; padding: 0; }
  html, body {
    width: 731px;
    height: 1200px;
    overflow: hidden;
    background: var(--page-bg);
    font-family: "Poppins", sans-serif;
  }
  .lawn-sign {
    position: absolute;
    left: 40px;
    top: 356px;
    width: 651px;
    height: 488px;
    background: var(--paper);
    box-shadow: 0 10px 18px rgba(0, 0, 0, 0.35);
    display: flex;
    flex-direction: column;
  }
  .brand-panel {
    position: relative;
    height: 242px;
    background: var(--ink-black);
  }
  .drip-band {
    position: absolute;
    left: 0; top: 0;
    width: 100%;
    height: 84px;
    background: linear-gradient(180deg, var(--drip-light) 0%, var(--drip-deep) 100%);
  }
  .brand-name {
    position: absolute;
    left: 0; right: 0;
    top: 110px;
    text-align: center;
    color: var(--brand-blue);
    font-weight: 800;
    text-transform: uppercase;
    line-height: 1;
  }
  .brand-name .line-main {
    display: block;
    font-size: 62px;
    letter-spacing: 4px;
  }
  .brand-name .line-sub {
    display: block;
    margin-top: 8px;
    font-size: 38px;
    letter-spacing: 18px;
    padding-left: 18px;
  }
  .services {
    height: 103px;
    background: var(--sun-yellow);
    display: flex;
    align-items: center;
    padding: 10px 0;
  }
  .service-group {
    list-style: none;
    height: 82px;
    display: flex;
    flex-direction: column;
    justify-content: center;
    gap: 4px;
    color: var(--text-dark);
    font-weight: 600;
    font-size: 24px;
    line-height: 1.2;
  }
  .service-group + .service-group { border-left: 1px dashed #555; }
  .service-group.first { width: 207px; padding-left: 40px; }
  .service-group.second { width: 236px; padding-left: 28px; }
  .service-group.third { flex: 1; padding-left: 26px; }
  .service-group li { display: flex; align-items: center; gap: 12px; }
  .service-group .wrap-line { padding-left: 26px; margin-top: -4px; }
  .tick { width: 14px; height: 14px; flex: none; }
  .divider { height: 4px; background: var(--paper); }
  .phone-bar {
    height: 63px;
    background: var(--berry);
    display: flex;
    align-items: center;
    justify-content: center;
    gap: 12px;
    color: var(--paper);
  }
  .phone-icon { width: 44px; height: 44px; }
  .phone-number {
    font-size: 46px;
    font-weight: 800;
    letter-spacing: 2px;
    line-height: 1;
  }
  .call-to-action {
    flex: 1;
    display: flex;
    justify-content: center;
    padding-top: 14px;
    font-size: 22px;
    font-weight: 700;
    letter-spacing: 7.5px;
    color: var(--text-dark);
    text-transform: uppercase;
  }
</style>
</head>
<body>
  <section class="lawn-sign">
    <header class="brand-panel">
      <div class="drip-band" role="img" aria-label="Dripping golden paint decoration along the top edge"></div>
      <h1 class="brand-name">
        <span class="line-main">Quillmark</span>
        <span class="line-sub">Painting</span>
      </h1>
    </header>

    <div class="services">
      <ul class="service-group first">
        <li><svg class="tick" viewBox="0 0 14 14"><circle cx="7" cy="7" r="7" fill="#12b2e6"/><path d="M3.8 7.2l2.2 2.1 4.3-4.4" stroke="#fff" stroke-width="1.8" fill="none" stroke-linecap="round" stroke-linejoin="round"/></svg>Interior</li>
        <li><svg class="tick" viewBox="0 0 14 14"><circle cx="7" cy="7" r="7" fill="#12b2e6"/><path d="M3.8 7.2l2.2 2.1 4.3-4.4" stroke="#fff" stroke-width="1.8" fill="none" stroke-linecap="round" stroke-linejoin="round"/></svg>Exterior</li>
      </ul>
      <ul class="service-group second">
        <li><svg class="tick" viewBox="0 0 14 14"><circle cx="7" cy="7" r="7" fill="#12b2e6"/><path d="M3.8 7.2l2.2 2.1 4.3-4.4" stroke="#fff" stroke-width="1.8" fill="none" stroke-linecap="round" stroke-linejoin="round"/></svg>Residential</li>
        <li><svg class="tick" viewBox="0 0 14 14"><circle cx="7" cy="7" r="7" fill="#12b2e6"/><path d="M3.8 7.2l2.2 2.1 4.3-4.4" stroke="#fff" stroke-width="1.8" fill="none" stroke-linecap="round" stroke-linejoin="round"/></svg>Commercial</li>
      </ul>
      <ul class="service-group third">
        <li><svg class="tick" viewBox="0 0 14 14"><circle cx="7" cy="7" r="7" fill="#12b2e6"/><path d="M3.8 7.2l2.2 2.1 4.3-4.4" stroke="#fff" stroke-width="1.8" fill="none" stroke-linecap="round" stroke-linejoin="round"/></svg>Pressure</li>
        <li class="wrap-line">washing</li>
      </ul>
    </div>

    <div class="divider"></div>

    <div class="phone-bar">
      <svg class="phone-icon" viewBox="0 0 44 44" aria-hidden="true">
        <circle cx="22" cy="22" r="22" fill="#fff"/>
        <path d="M15.5 11.5c1-.6 2.2-.3 2.8.7l2.2 3.6c.5.9.3 2-.5 2.6l-1.6 1.2c1 2.4 2.8 4.4 5.1 5.6l1.3-1.5c.7-.8 1.8-.9 2.6-.4l3.5 2.4c.9.6 1.2 1.9.6 2.8l-1.3 2c-.8 1.2-2.3 1.8-3.7 1.4-6.5-1.9-11.4-7.2-13-13.8-.3-1.4.3-2.8 1.5-3.6z" fill="#ae1a6b"/>
        <path d="M24 12.5a8 8 0 0 1 7.5 7.5M24 16.5a4 4 0 0 1 3.5 3.5" stroke="#ae1a6b" stroke-width="1.8" fill="none" stroke-linecap="round"/>
      </svg>
      <span class="phone-number">+1(204)555-0187</span>
    </div>

    <p class="call-to-action">Call us now for free estimates</p>
  </section>
</body>
</html>
```